Tobin's Butter dairy product for export market

We are starting a new brand for our butter range. We are looking for a premimum branding with family values. The product should be elligent and simle and easy for consumers to choose and easy for chefs,

A samples of our current brand and packing details in on the pack
target markets , China, Hong Kong, Asia, middle east
products will be sold in different size starting from small portion eg 7g to 1kg food service pack
product will be sold in 2 varients salted and unsalted

Target Market(s)

Australian Market and export market

Industry/Entity Type

Product

Colors
9bcb3c
fbed22

Requirements
Must have
• Pure butter
• packed in Australia
• nice fresh modern simple design
Nice to have
• Colours gold , green or any other suggestions welcome.
Should not have
• Any third party pictures of butter etc..

```html
<!DOCTYPE html>
<html lang="en">
<head>
<meta charset="UTF-8">
<title>Tobin's Butter – Portion Lids</title>
<link rel="stylesheet" href="https://fonts.googleapis.com/css2?family=Cinzel:wght@700&display=swap">
<style>
  :root {
    --bg: #f1f0f3;
    --salted-green: #9bcb3c;
    --salted-green-deep: #86b82c;
    --unsalted-yellow: #fbed22;
    --unsalted-yellow-deep: #f2d90f;
    --ink-green: #1f6a2c;
    --burst-light: #fff59a;
    --butter-gold: #f7d417;
    --cream: #ffffff;
  }
  * { box-sizing: border-box; margin: 0; padding: 0; }
  html, body {
    width: 1200px;
    height: 864px;
    overflow: hidden;
  }
  body {
    background: var(--bg);
    display: flex;
    align-items: center;
    justify-content: center;
    gap: 110px;
    font-family: "Cinzel", Georgia, serif;
  }
  .lid {
    position: relative;
    width: 400px;
    height: 400px;
    border-radius: 34px;
    overflow: hidden;
    box-shadow: 0 14px 30px rgba(0, 0, 0, 0.12);
  }
  .lid--salted {
    background: linear-gradient(135deg, var(--salted-green) 0%, var(--salted-green-deep) 100%);
  }
  .lid--unsalted {
    background: linear-gradient(135deg, var(--unsalted-yellow) 0%, var(--unsalted-yellow-deep) 100%);
  }
  .lid__artwork {
    position: absolute;
    left: 50%;
    top: 46%;
    width: 250px;
    height: 210px;
    transform: translate(-50%, -50%);
    border-radius: 50%;
    background: radial-gradient(circle at 50% 50%,
      var(--butter-gold) 0%,
      var(--butter-gold) 30%,
      var(--cream) 46%,
      var(--burst-light) 62%,
      rgba(255, 245, 154, 0) 72%);
  }
  .lid__brand {
    position: absolute;
    left: 0;
    right: 0;
    top: 128px;
    text-align: center;
    font-size: 64px;
    font-weight: 700;
    color: var(--ink-green);
    letter-spacing: 0.01em;
  }
  .lid__variant {
    position: absolute;
    left: 0;
    right: 0;
    bottom: 58px;
    text-align: center;
    font-size: 21px;
    font-weight: 700;
    color: var(--ink-green);
    letter-spacing: 0.22em;
  }
</style>
</head>
<body>
  <article class="lid lid--salted">
    <div class="lid__artwork" role="img" aria-label="Illustration of a butter block bursting from a white cloud with sun rays"></div>
    <h1 class="lid__brand">Tobin's</h1>
    <p class="lid__variant">Salted Butter</p>
  </article>

  <article class="lid lid--unsalted">
    <div class="lid__artwork" role="img" aria-label="Illustration of a butter block bursting from a white cloud with sun rays"></div>
    <h2 class="lid__brand">Tobin's</h2>
    <p class="lid__variant">Unsalted Butter</p>
  </article>
</body>
</html>
```